Business Card Design Project

I am looking for a classy business card design for a product design consultancy. We specialize in Product Design, Prototyping, and Manufacturing Consulting. Products that we design range from consumer electronics to household products all the way to sporting goods. We are based in Arizona and called "Pelican Forge Studio." We like to have fun and goof off as much as we like to create new products. We are young and energetic so we would like our business cards to reflect that. We already have a logo that we would like to implement into the card design. A plain rectangular business card is boring so feel free to get creative, but please, no avocado shaped cards (it's far too literal). Also feel free to play around with textured card stocks or plastic. The final design that we choose will pay attention to all of the little details. Our cards will need to be 2 sided. We're giving you guys free reign to design as you would like. Please have fun with this, it will reflect in our business card.

Thanks guys,
Pelican Forge Studio Team
Updates

Industry/Entity Type

Electronics

Requirements
Must have
• We would like to have a spot UV coating somewhere on the business card design if possible.
Nice to have
• Let's see some designs with custom shapes rather than typical rectangular business cards but please no avocado shaped cards, thanks. Also play around with textured card socks.

Files

```html
<!DOCTYPE html>
<html lang="en">
<head>
<meta charset="UTF-8">
<title>Pelican Forge Studio – Business Card</title>
<link rel="stylesheet" href="https://fonts.googleapis.com/css2?family=Comfortaa:wght@300;400&family=Questrial&display=swap">
<style>
  :root {
    --page: #ffffff;
    --card-center: #ffffff;
    --card-edge: #d6efa6;
    --lime: #9ee02c;
    --lime-soft: #a8e64a;
    --ink: #2f3433;
    --grey: #8c969b;
  }
  html, body {
    margin: 0;
    padding: 0;
    width: 1200px;
    height: 349px;
    overflow: hidden;
    background: var(--page);
  }
  .sheet {
    position: relative;
    width: 1200px;
    height: 349px;
  }
  .card {
    position: absolute;
    top: 1px;
    height: 346px;
    background: radial-gradient(ellipse at 55% 50%, var(--card-center) 0%, #f3fbe6 35%, var(--card-edge) 100%);
    overflow: hidden;
  }
  .card--front { left: 0; width: 578px; }
  .card--back  { left: 621px; width: 579px; background: radial-gradient(ellipse at 40% 40%, var(--card-center) 0%, #f1fae2 40%, var(--card-edge) 100%); }

  .brand {
    position: absolute;
    left: 52px;
    top: 140px;
    display: flex;
    align-items: center;
    gap: 18px;
  }
  .brand__dot {
    width: 64px;
    height: 64px;
    border-radius: 50%;
    background: var(--lime);
    flex: none;
  }
  .brand__name {
    font-family: "Questrial", sans-serif;
    font-size: 39px;
    color: var(--lime);
    white-space: nowrap;
  }

  .back__dot {
    position: absolute;
    left: 52px;
    top: 72px;
    width: 74px;
    height: 74px;
    border-radius: 50%;
    background: var(--lime);
  }
  .back__heading {
    position: absolute;
    right: 28px;
    top: 42px;
    margin: 0;
    font-family: "Comfortaa", sans-serif;
    font-weight: 400;
    font-size: 35px;
    color: var(--lime-soft);
    letter-spacing: 1px;
  }
  .contact {
    position: absolute;
    right: 28px;
    top: 112px;
    text-align: right;
    font-family: "Questrial", sans-serif;
    color: var(--ink);
  }
  .contact__name {
    font-size: 19px;
    margin: 0 0 8px;
  }
  .contact__line {
    font-size: 16.5px;
    margin: 0;
    line-height: 22.5px;
  }
  .services {
    position: absolute;
    left: 43px;
    top: 258px;
    margin: 0;
    font-family: "Questrial", sans-serif;
    font-size: 16.5px;
    color: var(--ink);
    white-space: nowrap;
  }
</style>
</head>
<body>
  <main class="sheet">
    <section class="card card--front" aria-label="Card front">
      <div class="brand">
        <span class="brand__dot"></span>
        <span class="brand__name">Pelican Forge Studio</span>
      </div>
    </section>

    <section class="card card--back" aria-label="Card back">
      <span class="back__dot"></span>
      <h1 class="back__heading">get in touch</h1>
      <div class="contact">
        <p class="contact__name">Dana Whitlow / President</p>
        <p class="contact__line">Office: 480.555.0142</p>
        <p class="contact__line">Cell: 602.555.0187</p>
        <p class="contact__line">Email: dana@pelicanforgestudio.com</p>
        <p class="contact__line">Web: www.pelicanforgestudio.com</p>
      </div>
      <p class="services">Product Design ~ Prototyping ~Manufacturing Consulting</p>
    </section>
  </main>
</body>
</html>
```